Refresh Home Page for Photography Training Site

http://brannowlessons.example/

My site is looking kind of out-of-date, so it's time for a face lift. I want to bring it up to date with a more modern web look.

What I need from you is a home page design concept. No coding, just a PSD design, but it MUST be something that a coder could build into an efficient, fast-loading page. After the home page design contest is finished, we can work together privately, if you want to continue, to design the rest of the pages in the site for additional fees.

Functionally, the new page needs to do the same job as the current home page, just do it more efficiently (if possible) while looking fresh and modern.

Sites I like
http://quelt.example/ (clean, modern)

Competitor sites:
http://varnocourses.example/
http://www.ivanmorrowimaging.example/

Target Market(s)

Amateur and semi-professional photographers

Industry/Entity Type

Training

Requirements
Must have
• MUST HAVE
1. A prominent space where testimonials appear in rotation, one after another (instead of the one large testimonial on the current site).

2. My photo in the header. It can be smaller than at present. If you prefer you can use the black and white photo from the about page. Put a signature saying Dan Brannow near the photo, in a better handwritten style than the current signature, which is a lame font.

3. Tagline "Learn Photography and Image Editing the Easy Way"
Should not have
• No flash or other fancy technology. (However it is acceptable to design an area that would be an image carousel, where one image changes to another, then another, etc. Like the Ivan Morrow or Quelt site. That is not too fancy, but it's optional).

```html
<!DOCTYPE html>
<html lang="en">
<head>
<meta charset="utf-8">
<title>Brannow Training – Learn Photography and Image Editing the Easy Way</title>
<link rel="stylesheet" href="https://fonts.googleapis.com/css2?family=Arimo:wght@400;700&display=swap">
<style>
:root{
  --ink:#333333;
  --ink-soft:#555555;
  --ink-muted:#666666;
  --accent-red:#cc1111;
  --accent-blue:#1f4d6e;
  --line:#cfcfcf;
  --page:#ffffff;
  --nav-top:#fdfdfd;
  --nav-bottom:#e4e4e4;
  --band-top:#dde8f8;
  --band-bottom:#ffffff;
  --button-top:#ffffff;
  --button-bottom:#dbe6f6;
  --link:#7a1010;
  --social:#3b5a99;
}
*{box-sizing:border-box;margin:0;padding:0}
html,body{width:1200px;height:2400px;overflow:hidden;background:var(--page)}
body{position:relative;font-family:"Arimo",Arial,sans-serif;color:var(--ink)}
.abs{position:absolute}
.photo{position:absolute;display:block}
a{text-decoration:none}

/* header */
.header-portrait{left:0;top:0;width:140px;height:140px;background:linear-gradient(160deg,#e9dcc8,#b98d6a 55%,#6d5a4c)}
.brand{left:190px;top:28px;font-size:62px;line-height:1;color:#6a6a6a;font-weight:400;letter-spacing:1px;white-space:nowrap}
.tagline{left:206px;top:106px;font-size:17px;color:var(--ink-soft);white-space:nowrap}
.header-camera{left:1054px;top:0;width:146px;height:140px;background:linear-gradient(160deg,#d7dbe0,#40464d 60%,#1c1e22)}

/* navigation */
.nav{left:4px;top:146px;width:1192px;height:56px;border:1px solid var(--line);border-radius:6px;background:linear-gradient(var(--nav-top),var(--nav-bottom))}
.nav a{position:absolute;top:0;height:54px;line-height:54px;font-size:17px;color:#222;white-space:nowrap}
.nav .is-active{left:34px;width:104px;text-align:center;background:linear-gradient(#e2e2e2,#cfcfcf)}
.search{left:896px;top:8px;width:238px;height:36px;border:1px solid #bdbdbd;border-radius:18px;background:#fff}
.search-go{left:1150px;top:0;line-height:54px;font-size:17px}

/* hero carousel */
.hero{left:2px;top:218px;width:1196px;height:414px;overflow:hidden}
.hero-slide{top:0;height:414px}
.hero-arrow{top:168px;width:40px;height:70px;background:#1d1d1d;border-radius:4px}

/* testimonial */
.quote{left:36px;top:672px;font-size:28px;line-height:56px;color:#2d2d2d;white-space:nowrap}
.quote-line{display:block}
.quote-line.is-second{padding-left:46px}
.quote-mark{font-size:50px;color:#777;vertical-align:-14px;font-family:Georgia,serif}
.quote-by{left:686px;top:750px;font-size:22px;color:var(--accent-blue);white-space:nowrap}
.testimonial-camera{left:940px;top:636px;width:140px;height:144px;border-radius:50%;background:radial-gradient(circle at 45% 55%,#6b7784,#1a1c1f 60%,#fff 72%)}
.divider{left:0;top:800px;width:1200px;height:18px;background:radial-gradient(ellipse at 50% 0,rgba(0,0,0,.28),rgba(0,0,0,0) 70%)}

/* free tutorials */
.section-title{font-size:30px;color:#333;font-weight:400;white-space:nowrap}
.card{top:924px;width:326px;height:346px;border:1px solid #bfbfbf;border-radius:8px;background:#fff;box-shadow:0 2px 4px rgba(0,0,0,.12)}
.card-title{position:absolute;left:0;top:0;width:100%;height:52px;line-height:52px;text-align:center;font-size:22px;font-weight:400;border-bottom:1px dashed #ccc;white-space:nowrap}
.card-art{left:92px;top:62px;width:142px;height:142px;border-radius:8px}
.card-free{position:absolute;left:12px;top:178px;font-size:17px;color:var(--accent-red)}
.card-text{position:absolute;left:12px;top:222px;width:310px;font-size:13.6px;line-height:21px;color:var(--ink)}
.card-view{position:absolute;right:0;bottom:0;width:118px;height:40px;line-height:40px;text-align:center;font-size:17px;color:var(--link);border:1px solid #c6c6c6;border-radius:6px 0 8px 0;background:#fff}

/* course features */
.band{height:52px;background:linear-gradient(var(--band-top),var(--band-bottom));text-align:center;font-size:22px;font-weight:400;color:#222;white-space:nowrap}
.feature-text{font-size:14px;line-height:21px;color:var(--ink)}
.feature-text p{margin-bottom:20px}
.learn-more{width:146px;height:44px;line-height:44px;text-align:center;font-size:15px;color:var(--link);background:linear-gradient(var(--button-top),var(--button-bottom));border-radius:4px}

/* videos */
.video{left:848px;width:306px;height:186px}
.play{left:118px;top:72px;width:70px;height:44px;background:rgba(0,0,0,.85)}
.video-caption{left:826px;width:350px;text-align:center;font-size:14px;color:var(--ink);white-space:nowrap}

/* other works */
.works{left:30px;top:2090px;width:1140px;height:190px;border:1px solid #c9c9c9;border-radius:8px;background:linear-gradient(#ffffff,#e7e7e7)}
.works-thumb{top:16px;height:156px;box-shadow:0 2px 4px rgba(0,0,0,.35)}
.works-arrow{top:80px;width:26px;height:26px;border-radius:50%;background:#3a3a3a}

/* footer */
.social-bar{left:48px;top:2296px;width:364px;height:30px;background:#eef0f5;border-radius:3px}
.social-btn{top:4px;height:22px;border:1px solid #aab3c8;border-radius:3px;background:#fff;font-size:13px;line-height:20px;padding:0 6px;color:var(--social)}
.social-square{top:2346px;width:36px;height:36px;border-radius:6px}
.footer-links{left:540px;top:2322px;width:370px;text-align:center;font-size:14px;white-space:nowrap}
.footer-links a{color:var(--ink)}
.copyright{left:500px;top:2362px;width:450px;text-align:center;font-size:14px;white-space:nowrap}
</style>
</head>
<body>

<header>
  <div class="photo header-portrait abs" role="img" aria-label="Portrait of Dan Brannow"></div>
  <div class="brand abs">Brannow Training</div>
  <div class="tagline abs">Learn Photography and Image Editing the Easy Way</div>
  <div class="photo header-camera abs" role="img" aria-label="Video camera with film strip"></div>
</header>

<nav class="nav abs">
  <a class="is-active" href="#">Home</a>
  <a style="left:164px" href="#">Courses</a>
  <a style="left:282px" href="#">Free Tutorials</a>
  <a style="left:446px" href="#">About</a>
  <a style="left:546px" href="#">Contact</a>
  <a style="left:660px" href="#">Login</a>
  <div class="search abs">
    <svg class="abs" style="left:200px;top:5px" width="26" height="26" viewBox="0 0 26 26"><circle cx="11" cy="11" r="7" fill="none" stroke="#8a8a8a" stroke-width="2.5"/><line x1="16" y1="16" x2="23" y2="23" stroke="#8a8a8a" stroke-width="3" stroke-linecap="round"/></svg>
  </div>
  <span class="search-go abs">Go</span>
</nav>

<section class="hero abs" aria-label="Featured photographs">
  <div class="photo hero-slide" style="left:0;width:378px;background:linear-gradient(#3c3c3c,#8a8a8a 45%,#2e2e2e)" role="img" aria-label="Wedding couple under a stormy sky"></div>
  <div class="photo hero-slide" style="left:378px;width:396px;background:linear-gradient(#d6ecf7,#7ec5e6 50%,#c7a58a)" role="img" aria-label="Hands forming a peace sign against the sky"></div>
  <div class="photo hero-slide" style="left:774px;width:422px;background:linear-gradient(#1f5fb4,#6da2d8 45%,#3c5570)" role="img" aria-label="Two people leaping on a beach near a pier"></div>
  <svg class="abs" style="left:0;top:360px" width="1196" height="54" viewBox="0 0 1196 54" aria-hidden="true"><path d="M0 30 Q300 62 598 34 T1196 14 V54 H0 Z" fill="#fff"/></svg>
  <div class="hero-arrow abs" style="left:-2px"><svg width="40" height="70" viewBox="0 0 40 70"><path d="M24 27 L14 35 L24 43" fill="none" stroke="#fff" stroke-width="3"/></svg></div>
  <div class="hero-arrow abs" style="left:1158px"><svg width="40" height="70" viewBox="0 0 40 70"><path d="M16 27 L26 35 L16 43" fill="none" stroke="#fff" stroke-width="3"/></svg></div>
</section>

<section aria-label="Testimonials">
  <p class="quote abs">
    <span class="quote-line"><span class="quote-mark">“</span> I Love Your videos! I can learn more in one hour than in a month</span>
    <span class="quote-line is-second">of studying photography books! <span class="quote-mark">”</span></span>
  </p>
  <p class="quote-by abs">- Karen D Denver CO</p>
  <div class="photo testimonial-camera abs" role="img" aria-label="Digital SLR camera"></div>
  <div class="divider abs"></div>
</section>

<section aria-label="Free Photo Tutorials">
  <h2 class="section-title abs" style="left:60px;top:850px">Free Photo Tutorials</h2>

  <article class="card abs" style="left:52px">
    <h3 class="card-title">Understanding Depth of Field</h3>
    <div class="photo card-art abs" style="background:linear-gradient(135deg,#7cc3f2,#2a5ea8 50%,#222)" role="img" aria-label="Camera with photo prints"></div>
    <span class="card-free">Free!</span>
    <p class="card-text">One of the most important elements of<br>photography is also one of the least understood.<br>Learn how you can use depth of field to take<br>better photos!</p>
    <a class="card-view" href="#">View</a>
  </article>

  <article class="card abs" style="left:436px">
    <h3 class="card-title">Flash Photography Tips</h3>
    <div class="photo card-art abs" style="background:linear-gradient(135deg,#e0422a,#5a9b3a 55%,#222)" role="img" aria-label="Camera with a flower print"></div>
    <span class="card-free">Free!</span>
    <p class="card-text">One of the most important elements of<br>photography is also one of the least understood.<br>Learn how you can use depth of field to take<br>better photos!</p>
    <a class="card-view" href="#">View</a>
  </article>

  <article class="card abs" style="left:822px">
    <h3 class="card-title">PixelForge Layer Blending</h3>
    <div class="photo card-art abs" style="background:linear-gradient(135deg,#e23a9c,#7b2fb8 50%,#222)" role="img" aria-label="Colourful stacked layer graphic"></div>
    <span class="card-free">Free!</span>
    <p class="card-text">One of the most important elements of<br>photography is also one of the least understood.<br>Learn how you can use depth of field to take<br>better photos!</p>
    <a class="card-view" href="#">View</a>
  </article>
</section>

<section aria-label="Courses">
  <h2 class="band abs" style="left:56px;top:1300px;width:714px;height:84px;padding-top:10px;line-height:32px">How to Shoot Professional-Looking Headshots and Portraits<br>on a Budget with Small Flashes</h2>
  <div class="photo abs" style="left:82px;top:1400px;width:246px;height:212px;background:linear-gradient(135deg,#2b5fb0,#c9a58a 55%,#2a2a2a)" role="img" aria-label="Photographer holding a camera"></div>
  <div class="feature-text abs" style="left:356px;top:1408px;width:420px">
    <p>Want to make extra money with your digital SLR?</p>
    <p>Or would you simply like to take professional-looking portraits<br>without spending a fortune on equipment?</p>
    <p>This 9-video course, will teach you all you need to know about<br>off-camera lighting with your digital SLR's<br>detachable flash!</p>
    <p>Start taking better photos today!</p>
  </div>
  <a class="learn-more abs" style="left:630px;top:1614px" href="#">Learn more</a>

  <h2 class="band abs" style="left:56px;top:1720px;width:714px;line-height:52px">Lumaroll Basics for Photographers</h2>
  <div class="photo abs" style="left:92px;top:1786px;width:206px;height:208px;border:2px solid #c41a1a;background:radial-gradient(circle at 50% 45%,#b44a2a,#5a1010 50%,#120404)" role="img" aria-label="Portrait of a woman in a red scarf"></div>
  <div class="feature-text abs" style="left:356px;top:1796px;width:420px">
    <p>Lumaroll Studio is the premiere software for organizing, cataloguing<br>and editing your digital photos.</p>
    <p>Learn how Lumaroll can help you take your photography to the next<br>level in this introductory video course.</p>
    <p>Join the free tutorial mailing list to be notified when this course is<br>released.</p>
  </div>
  <a class="learn-more abs" style="left:628px;top:1988px" href="#">Learn more</a>
</section>

<aside aria-label="Photography Video Tutorials">
  <h2 class="band abs" style="left:826px;top:1300px;width:340px;height:40px;line-height:40px">Photography Video Tutorials</h2>

  <div class="photo video abs" style="top:1350px;background:linear-gradient(135deg,#5a1a0c,#d0552a 50%,#6a220f)" role="img" aria-label="Red canyon walls">
    <div class="play abs"><svg width="70" height="44" viewBox="0 0 70 44"><path d="M28 12 L44 22 L28 32 Z" fill="#fff"/></svg></div>
  </div>
  <p class="video-caption abs" style="top:1540px">12 Common Photography Mistakes Beginners Do</p>

  <div class="photo video abs" style="top:1584px;background:linear-gradient(#e6e2d6,#8a8a70 45%,#4a7a2e)" role="img" aria-label="Family sitting on a lawn before a house">
    <div class="play abs"><svg width="70" height="44" viewBox="0 0 70 44"><path d="M28 12 L44 22 L28 32 Z" fill="#fff"/></svg></div>
  </div>
  <p class="video-caption abs" style="top:1784px">Family Photography Tips</p>

  <div class="photo video abs" style="top:1824px;background:linear-gradient(135deg,#0c0c0c,#8a8a8a 50%,#111)" role="img" aria-label="Black and white beauty portrait">
    <div class="play abs"><svg width="70" height="44" viewBox="0 0 70 44"><path d="M28 12 L44 22 L28 32 Z" fill="#fff"/></svg></div>
  </div>
  <p class="video-caption abs" style="top:2020px">How To Create Porcelain Skin On PixelForge</p>
</aside>

<section aria-label="View Other Works">
  <h2 class="abs" style="left:48px;top:2050px;font-size:22px;font-weight:400;white-space:nowrap">View Other Works</h2>
  <div class="works abs">
    <div class="works-arrow abs" style="left:22px"><svg width="26" height="26" viewBox="0 0 26 26"><path d="M15 8 L10 13 L15 18 Z" fill="#fff"/></svg></div>
    <div class="photo works-thumb" style="left:62px;width:186px;background:linear-gradient(135deg,#fff,#e23a1a 50%,#a01010)" role="img" aria-label="Red liquid splash"></div>
    <div class="photo works-thumb" style="left:264px;width:188px;background:radial-gradient(circle,#e0532a,#6a150a 60%,#0a0a0a)" role="img" aria-label="Red coral tentacles"></div>
    <div class="photo works-thumb" style="left:468px;width:186px;background:radial-gradient(circle,#8fc3e8,#2a5a20 55%,#0c200c)" role="img" aria-label="Looking up through trees"></div>
    <div class="photo works-thumb" style="left:672px;width:186px;background:linear-gradient(135deg,#f0c2a0,#c46a3a 50%,#3d6aa8)" role="img" aria-label="Couple lying together"></div>
    <div class="photo works-thumb" style="left:876px;width:188px;background:linear-gradient(135deg,#0a0a0a,#8ab6e0 50%,#0a0a0a)" role="img" aria-label="Stacked image layers on black"></div>
    <div class="works-arrow abs" style="left:1092px"><svg width="26" height="26" viewBox="0 0 26 26"><path d="M11 8 L16 13 L11 18 Z" fill="#fff"/></svg></div>
  </div>
</section>

<footer>
  <div class="social-bar abs">
    <span class="social-btn abs" style="left:6px">Like</span>
    <span class="social-btn abs" style="left:58px">Send</span>
    <span class="abs" style="left:112px;top:7px;font-size:13px;color:var(--social);white-space:nowrap">313 people like this.</span>
    <span class="social-btn abs" style="left:300px;width:26px;padding:0"></span>
    <span class="social-btn abs" style="left:330px;color:#444">1</span>
  </div>
  <span class="social-square abs" style="left:52px;background:#3b5a99" aria-label="Social profile"></span>
  <span class="social-square abs" style="left:104px;background:#3aa3d8" aria-label="Social profile"></span>
  <span class="social-square abs" style="left:156px;background:#1f6fa8" aria-label="Social profile"></span>
  <span class="social-square abs" style="left:208px;background:#e2661c" aria-label="Social profile"></span>

  <p class="footer-links abs"><a href="#">Terms &amp; Conditions</a> &nbsp;|&nbsp; <a href="#">Privacy Policy</a> &nbsp;|&nbsp; <a href="#">Contact</a></p>
  <p class="copyright abs">Copyright© 2011 &nbsp;Brannow Training, All Rights Reserved</p>
</footer>

</body>
</html>
```